Recruitment company website redesign

We're looking to redesign our current website, located at http://www.crestwayhire.com.au, to make it more FRESH, modern, easy-to-navigate, and user-friendly. Navigation should be very obvious, and buttons should be big. The design should be closer to the flat/clean look of Zorvik or Qelt9 rather than the somewhat older embossed look.

The design also needs to take into consideration that the coding will be responsive (mobile, tablet, etc.-friendly).

We'd like to see your work on two pages, and from there, we'll choose a designer that we will pay further to design the rest of the site. The two pages we will need are:

1. A home page, with the content detailed in the attached image home-outline.jpg. Keep in mind that this is a very rough outline with no design whatsoever, so please take those elements and create a beautiful page from it. Feel free to move the content around if necessary, as long as that's all on there. We're pretty open to whatever you think would look best.

Using high quality images could look great, and we'd purchase the perfect stock photos down the line, but for now just use any business-related images that aren't too cheesy (stay away from anything that looks too stock image-y like smiling actors).

2. A talent dashboard. This will live as a separate microsite; therefore, the design should be consistent with the home page but also be separate. Here, you have some more freedom with the design, but use our overall style and make it look like a user dashboard - very simple and easy to translate for responsive design.

There should be a horizontal menu that includes: "Edit Profile," "Apply for a Job," "WHS" (this will have a drop-down submenu), "My History" (also with a drop-down submenu), and "Contact."

Above that menu should be a place for users to sign in/out. Below the menu will be a welcome message and then a notice board for our updates.

Reason: Still haven't found the perfect design.

Hi designers,

We will make a decision Monday and let you know. Thanks for your submissions!

Industry/Entity Type

Business

Font styles to use
Sans Serif

Colors
33b7a4
f78f20
ffffff

Requirements
Must have
• Please use our current color scheme, fonts, and logo. Attached is our logo and style guidelines. Not included in those style guidelines is the orange we also incorporate into our designs, which is #ff9a00.

Also have a look at http://www.crestwayhire.com.au, http://www.crestwayhire.com.au/blog, and http://www.linkvora.com/crestwayhirerecruitment. We want to take our current look and just modernize it a bit.

```html
<!DOCTYPE html>
<html lang="en">
<head>
<meta charset="utf-8">
<title>Crestway Hire – Home</title>
<link href="https://fonts.googleapis.com/css2?family=Roboto:wght@300;400;700&family=Roboto+Condensed:wght@300&display=swap" rel="stylesheet">
<style>
:root{
  --teal:#05a0b4;
  --teal-light:#5fc3cf;
  --nav-grey:#6d6e72;
  --bar-grey:#77787c;
  --text-dark:#333;
  --text-body:#555;
  --footer:#303236;
  --footer-bottom:#2c2e31;
  --footer-text:#c9cacc;
  --white:#fff;
}
*{margin:0;padding:0;box-sizing:border-box}
html,body{width:678px;height:1200px;overflow:hidden;background:var(--white)}
body{position:relative;font-family:"Roboto",Arial,sans-serif;color:var(--text-dark)}
.abs{position:absolute}
.brand{left:22px;top:10px;font-weight:300;font-size:37px;color:var(--teal);letter-spacing:-1px;display:flex;align-items:center;gap:6px}
.brand-dot{width:22px;height:22px;background:var(--nav-grey);border-radius:3px}
.social{display:flex;gap:6px}
.social span{display:block;width:20px;height:20px;border-radius:50%;background:var(--teal)}
.header-social{left:525px;top:13px}
.header-phone{left:525px;top:36px;font-size:17px;font-weight:300;color:#444}
.main-nav{left:0;top:70px;width:678px;height:36px;background:var(--nav-grey);font-weight:300;font-size:16px;color:var(--white)}
.main-nav a{position:absolute;top:0;line-height:36px;color:var(--white);text-decoration:none}
.main-nav .active{left:0;width:88px;background:var(--teal);text-align:center}
.hero-photo{left:0;top:106px;width:678px;height:316px;background:linear-gradient(120deg,#5d5048 0%,#a69789 45%,#d8d2cb 75%,#8a7d72 100%)}
.hero-box{left:14px;top:164px;width:299px;height:118px;background:rgba(238,239,241,.93);padding:15px 10px 0 18px;font-weight:300;font-size:15px;line-height:16.5px;color:#222}
.hero-video{left:14px;top:282px;width:299px;height:32px;background:rgba(100,100,104,.88);color:var(--white);font-weight:300;font-size:15.5px;line-height:32px;padding-left:57px}
.hero-video svg{position:absolute;left:35px;top:9px}
.action-band{left:0;top:422px;width:678px;height:127px;background:var(--teal)}
.action{position:absolute;top:388px;width:200px;text-align:center;color:var(--white);font-weight:300;font-size:20px}
.action svg{display:block;margin:0 auto 9px}
.section-bar{top:563px;height:31px;line-height:31px;color:var(--white);font-weight:300;font-size:17px;padding-left:30px}
.section-bar svg{position:absolute;left:12px;top:11px}
.jobs{top:608px;font-size:8.3px;line-height:10.4px;color:var(--text-body)}
.jobs h4{font-weight:700;color:#444;font-size:8.3px}
.jobs ul{list-style:none;margin-bottom:10.4px}
.companies{left:470px;top:615px;width:200px;display:grid;grid-template-columns:100px 100px;grid-auto-rows:35px;row-gap:15px}
.company{height:35px;display:flex;align-items:center;justify-content:center;font-weight:700;font-size:14px;color:#444}
.site-footer{left:0;top:916px;width:678px;height:192px;background:var(--footer);color:var(--white)}
.footer-col{position:absolute;top:34px}
.footer-col h3{font-weight:300;font-size:16px;margin-bottom:12px;letter-spacing:-.3px}
.footer-col p{font-size:7.6px;line-height:10px;color:var(--footer-text)}
.footer-social span{width:19px;height:19px;background:#bfc0c2}
.footer-phone{font-family:"Roboto Condensed",sans-serif;font-weight:300;font-size:19px;color:var(--footer-text);display:flex;align-items:center;gap:6px;margin-top:8px}
.footer-bottom{left:0;top:1108px;width:678px;height:92px;background:var(--footer-bottom);border-top:1px solid #3f4145;text-align:center;color:#8c8d90;font-size:7.6px;line-height:10.5px;padding-top:15px}
</style>
</head>
<body>
<header>
  <div class="abs brand">crestway<span class="brand-dot"></span>hire</div>
  <div class="abs social header-social"><span></span><span></span><span></span><span></span><span></span></div>
  <div class="abs header-phone">1-800-404-2271</div>
</header>
<nav class="abs main-nav">
  <a class="active" href="#">Home</a>
  <a href="#" style="left:127px">About</a>
  <a href="#" style="left:230px">Clients</a>
  <a href="#" style="left:338px">Candidates</a>
  <a href="#" style="left:476px">Blog</a>
  <a href="#" style="left:570px">Contact</a>
</nav>
<div class="abs hero-photo" role="img" aria-label="Photo of a businessman on a phone call working at a laptop"></div>
<div class="abs hero-box">Whether you are looking for your next career opportunity,or you are looking to recruit new people for your business. We believe in listening and tailoring our services to your needs.</div>
<div class="abs hero-video"><svg width="14" height="14" viewBox="0 0 14 14"><circle cx="7" cy="7" r="7" fill="#fff"/><circle cx="7" cy="7" r="5.5" fill="#2a8fe0"/><path d="M5.5 4.3v5.4L9.6 7z" fill="#fff"/></svg>Click here to watch Video</div>
<section>
  <div class="abs action-band"></div>
  <div class="action" style="left:96px">
    <svg width="96" height="96" viewBox="0 0 96 96"><circle cx="48" cy="48" r="47" fill="#fff"/><circle cx="48" cy="48" r="42" fill="var(--teal)"/><circle cx="48" cy="48" r="39" fill="#fff"/><circle cx="48" cy="48" r="36" fill="#e6e6e7"/><path d="M48 30l16 8v18l-16 8-16-8V38z" fill="#8b8c8f"/><path d="M32 38l16 8 16-8M48 46v18" stroke="#e6e6e7" stroke-width="2" fill="none"/></svg>
    FIND A JOB
  </div>
  <div class="action" style="left:380px">
    <svg width="96" height="96" viewBox="0 0 96 96"><circle cx="48" cy="48" r="47" fill="#fff"/><circle cx="48" cy="48" r="42" fill="var(--teal)"/><circle cx="48" cy="48" r="39" fill="#fff"/><circle cx="48" cy="48" r="36" fill="#e6e6e7"/><rect x="33" y="33" width="30" height="22" rx="3" fill="#6d6e72"/><rect x="36" y="36" width="24" height="16" fill="#e6e6e7"/><rect x="27" y="56" width="42" height="4" rx="2" fill="#6d6e72"/><path d="M47 41l5 6-3 .3 2 3-1 .6-2-3-2 2z" fill="#6d6e72"/></svg>
    FIND EMPLOYEES
  </div>
</section>
<div class="abs section-bar" style="left:9px;width:457px;background:var(--bar-grey)"><svg width="8" height="9"><path d="M0 0l8 4.5L0 9z" fill="#fff"/></svg>Browse Jobs</div>
<div class="abs section-bar" style="left:466px;width:206px;background:var(--teal-light)"><svg width="8" height="9"><path d="M0 0l8 4.5L0 9z" fill="#fff"/></svg>Featured Companies</div>
<div class="abs jobs" style="left:15px">
  <h4>Accounting / Finance</h4><ul><li>General/Cost Acct (2866)</li><li>Banking/Financial (1885)</li><li>Audit &amp; Taxation (793)</li><li>Finance/Investment (345)</li></ul>
  <h4>Admin / HR</h4><ul><li>Clerical/Administrative (2662)</li><li>Human Resources (1845)</li><li>Secretarial (725)</li><li>Top Management (83)</li></ul>
  <h4>Sales / Marketing</h4><ul><li>Retail Sales (2479)</li><li>Marketing (2472)</li><li>Sales - Corporate (1352)</li><li>Telesales/Telemarketing (1072)</li><li>Sales - Eng/Tech/IT (590)</li><li>Sales - Financial Services (305)</li><li>Merchandising (261)</li></ul>
</div>
<div class="abs jobs" style="left:178px">
  <h4>Computer / IT</h4><ul><li>Software (3467)</li><li>Network/Sys/DB (1976)</li><li>Hardware (1726)</li></ul>
  <h4>Engineering</h4><ul><li>Mechanical/Automotive (6530)</li><li>Other Eng (5245)</li><li>Electrical Eng (2865)</li><li>Electronics Eng (1526)</li><li>Environmental (619)</li><li>Oil/Gas Eng (487)</li><li>Industrial Eng (373)</li><li>Chemical Eng (345)</li></ul>
  <h4>Manufacturing</h4><ul><li>Manufacturing (3713)</li><li>Maintenance (1636)</li><li>Purchasing (1085)</li><li>Quality Assurance (985)</li><li>Process Design &amp; Control (200)</li></ul>
  <h4>Building / Construction</h4><ul><li>Civil Eng/Construction (4003)</li><li>Architect/Interior (1161)</li><li>Property/Real Estate (554)</li><li>Quantity Survey (462)</li></ul>
</div>
<div class="abs jobs" style="left:332px;top:611px">
  <h4>Arts / Media / Comm</h4><ul><li>Arts/Creative Design (1134)</li><li>Advertising (421)</li><li>Public Relations (234)</li><li>Entertainment (68)</li></ul>
  <h4>Services</h4><ul><li>Customer Service (8258)</li><li>Tech &amp; Helpdesk Support (1576)</li><li>Personal Care (1112)</li><li>Logistics/Supply Chain (616)</li><li>Security/Armed Forces (292)</li><li>Law/Legal Services (164)</li><li>Social Services (26)</li></ul>
  <h4>Hotel / Restaurant</h4><ul><li>F &amp; B (4734)</li><li>Hotel/Tourism (1956)</li></ul>
  <h4>Education / Training</h4><ul><li>Education (1367)</li><li>Training &amp; Dev. (486)</li></ul>
</div>
<div class="abs companies">
  <div class="company">Norvane</div><div class="company">Telbrook</div>
  <div class="company">Orvessa</div><div class="company">Halvern</div>
  <div class="company">Quarly</div><div class="company">Pimsel</div>
  <div class="company">Dovetrix</div>
</div>
<footer class="abs site-footer">
  <div class="footer-col" style="left:21px"><h3>NAVIGATION</h3><p style="padding-left:2px">Home<br>About Us<br>Clients<br>Candidates<br>Blog<br>Contact Us</p></div>
  <div class="footer-col" style="left:176px"><h3>LOCATIONS</h3><p>Chicago, IL , New York, NY ,<br>Boston, MA , Providence, RI ,<br>Hartford, CT, Philadelphia, PA,<br>Washington D.C., San Francisco, CA,<br>Seattle, WA , San Diego, CA,<br>Los Angeles, CA, Las Vegas, NV,<br>Denver, CO.</p></div>
  <div class="footer-col" style="left:362px"><h3>HELPS</h3><p>Privacy Policy<br>Terms of Use<br>Take a tour<br>For Employers<br>For Employees</p></div>
  <div class="footer-col" style="left:540px"><h3>CONNECT</h3>
    <div class="social footer-social" style="gap:7px"><span></span><span></span><span></span><span></span><span></span></div>
    <p style="margin-top:8px"><span style="font-size:9.5px;color:#fff">Crestway Hire</span><br>58 Alder Lane,<br>Westford, CT 06199</p>
    <div class="footer-phone"><svg width="18" height="18" viewBox="0 0 18 18"><circle cx="9" cy="9" r="8" fill="none" stroke="#c9cacc" stroke-width="1.3"/><path d="M6 5l2 2-1 1.2c.6 1.3 1.5 2.2 2.8 2.8L11 10l2 2-1.3 1.3C8.5 13 5 9.5 4.7 6.3z" fill="#c9cacc"/></svg>012-555-0148</div>
  </div>
</footer>
<div class="abs footer-bottom">©2013 Crestway Hire.com All Rights Reserved.<br><br>58 Alder Lane • Westford, CT 06199<br>Phone: 800-404-2271 • Fax: 860-555-0193</div>
</body>
</html>
```